Welcome E-Mail Design - UI/UX Designer

Hello All,

We are in the process of redesigning our complete webpage http://lnk.example-short.net/7QpTmR4.
While this, we are also looking to redesign our E-Mails.
The winner of the contest will be able to take the design of remaining E-Mail (more than 5)

I'm looking for an expert to work on Welcome E-Mail Design at the first place. If work delivery is as we expect, we would then assign the expert with other remaining E-Mails.

Here the text of welcome mail:
-------
Hi xxx,

We make it our mission to provide a reliable and safe gateway for services from Africa to the world.

Since we started in 2016, thousands of users have joined us on our journey to support our lovely continent.

We are happy to have you as our newest member:

Your User ID is <User's E-MAIL>

To fully activate your account, <a href="user's activation URL">login and follow the steps on the page </a>.

For any questions contact our Customer Care team at support@velunor-hq.com.

Best,
The team

---------

You can check in attachment our new design, which is not yet online.
Waiting for your proposal

Thanks in advance.

```html
<!DOCTYPE html>
<html lang="en">
<head>
<meta charset="utf-8">
<title>Velunor – Welcome email</title>
<link rel="stylesheet" href="https://fonts.googleapis.com/css2?family=Nunito+Sans:ital,wght@0,400;0,600;0,700;1,400&display=swap">
<style>
  :root {
    --page-bg: #eeeeef;
    --card-bg: #ffffff;
    --soft-band: #f6f8fc;
    --hero-top: #f4f5fb;
    --hero-bottom: #d3d9f2;
    --ink: #1c1c1c;
    --muted-ink: #5a6478;
    --italic-ink: #555a60;
    --brand-green: #12805c;
    --button: #f8ab35;
    --button-text: #ffffff;
    --dash: #a9a9a9;
    --icon-grey: #5b5b5b;
    --divider: #c9c9c9;
  }
  * { box-sizing: border-box; margin: 0; padding: 0; }
  html, body {
    width: 1200px; height: 2221px; overflow: hidden;
    background: var(--page-bg);
    font-family: "Nunito Sans", sans-serif;
    color: var(--ink);
  }
  .email {
    position: absolute; left: 76px; top: 76px;
    width: 1048px; height: 2069px;
    background: var(--card-bg);
  }
  .hero {
    position: absolute; left: 0; top: 0; width: 1048px; height: 413px;
    background: linear-gradient(180deg, var(--hero-top) 0%, var(--hero-top) 55%, var(--hero-bottom) 100%);
  }
  .hero-art {
    position: absolute; left: 400px; top: 20px; width: 640px; height: 393px;
    background: linear-gradient(180deg, rgba(211,217,242,0) 0%, rgba(190,199,236,0.55) 100%);
  }
  .brand {
    position: absolute; left: 135px; top: 174px; width: 246px;
    display: flex; align-items: center; gap: 10px;
  }
  .brand-mark {
    width: 26px; height: 26px; border-radius: 50%; background: var(--brand-green);
  }
  .brand-name {
    font-size: 42px; font-weight: 700; color: var(--ink); line-height: 1;
  }
  .social {
    position: absolute; left: 184px; top: 259px; display: flex; gap: 38px;
  }
  .social span {
    width: 22px; height: 22px; border-radius: 50%; background: var(--icon-grey);
  }
  .copy {
    position: absolute; left: 135px; width: 780px;
    font-size: 27px; line-height: 44px;
  }
  .greeting { top: 475px; color: var(--muted-ink); font-size: 28px; }
  .greeting strong { font-weight: 700; }
  .intro-1 { top: 553px; }
  .intro-2 { top: 803px; }
  .user-id {
    position: absolute; left: 0; top: 983px; width: 1048px; text-align: center;
  }
  .user-id-label { font-size: 29px; font-weight: 600; line-height: 44px; }
  .user-id-value {
    display: inline-block; margin-top: 6px; padding: 0 32px;
    border: 2px dashed var(--dash);
    font-size: 35px; line-height: 56px; color: var(--brand-green);
  }
  .user-id-note {
    font-size: 28px; font-style: italic; color: var(--italic-ink); line-height: 44px;
  }
  .activation {
    position: absolute; left: 0; top: 1151px; width: 1048px; height: 690px;
    background: var(--soft-band);
  }
  .activation-lead {
    position: absolute; left: 0; top: 60px; width: 1048px; text-align: center;
    font-size: 27px; line-height: 44px;
  }
  .activate-button {
    position: absolute; left: 211px; top: 133px; width: 625px; height: 77px;
    background: var(--button); border-radius: 5px;
    color: var(--button-text); font-size: 29px; font-weight: 600;
    display: flex; align-items: center; justify-content: center;
    text-decoration: none;
  }
  .activation-note {
    position: absolute; left: 130px; top: 234px; width: 788px; text-align: center;
    font-size: 27px; font-style: italic; line-height: 44px; color: var(--italic-ink);
  }
  .help { position: absolute; left: 135px; top: 384px; width: 780px; font-size: 27px; line-height: 44px; }
  .sign-off { position: absolute; left: 135px; top: 615px; font-size: 27px; line-height: 44px; }
  .sign-off strong { font-weight: 700; display: block; }
  .sign-off span { color: var(--brand-green); display: block; }
  .support {
    position: absolute; left: 0; top: 1901px; width: 1048px; text-align: center;
  }
  .support-title { font-size: 29px; font-weight: 600; color: var(--brand-green); line-height: 44px; }
  .support-line {
    margin-top: 29px; display: flex; justify-content: center; align-items: center;
    font-size: 28px; line-height: 36px;
  }
  .contact-item { display: flex; align-items: center; gap: 20px; }
  .contact-divider { width: 2px; height: 32px; background: var(--divider); margin: 0 24px; }
</style>
</head>
<body>
  <main class="email">
    <header class="hero">
      <div class="hero-art" role="img" aria-label="Illustration of a standing man holding a phone and a seated woman with a laptop sending banknotes to each other, in front of a pale blue town skyline"></div>
      <div class="brand">
        <span class="brand-mark"></span>
        <span class="brand-name">Velunor</span>
      </div>
      <div class="social" aria-label="Social links">
        <span></span><span></span><span></span>
      </div>
    </header>

    <p class="copy greeting">Welcome, <strong>LOREM</strong></p>
    <p class="copy intro-1">Thank you for choosing us. We make it our mission to provide a reliable and safe gateway for services from Africa to the world.</p>
    <p class="copy intro-2">Since we started in 2016, we are working hard on this mission. Thousands of users have joined us on our journey. We are happy to have you as our newest member!</p>

    <section class="user-id">
      <p class="user-id-label">Your User ID is</p>
      <p class="user-id-value">loremipsum@lorem.com</p>
      <p class="user-id-note">This ID functions as your username</p>
    </section>

    <section class="activation">
      <p class="activation-lead">To fully activate your account click button below:</p>
      <a class="activate-button" href="#">Login and follow the steps on the page</a>
      <p class="activation-note">It shouldn’t take more than a few minutes to fully activate your account. Then you will be able to deposit funds and start sending money to your loved ones.</p>
      <p class="help">For any questions you might have, our Customer Care team is here to help.</p>
      <p class="sign-off"><strong>Best,</strong><span>The team</span></p>
    </section>

    <footer class="support">
      <p class="support-title">Contact our support Team</p>
      <div class="support-line">
        <span class="contact-item">
          <svg width="30" height="30" viewBox="0 0 24 24" aria-hidden="true"><path fill="#111" d="M6.6 10.8a15.1 15.1 0 0 0 6.6 6.6l2.2-2.2c.3-.3.7-.4 1-.2 1.1.4 2.3.6 3.6.6.6 0 1 .4 1 1V20c0 .6-.4 1-1 1A17 17 0 0 1 3 4c0-.6.4-1 1-1h3.5c.6 0 1 .4 1 1 0 1.3.2 2.5.6 3.6.1.3 0 .7-.2 1z"/></svg>
          +237-655201384
        </span>
        <span class="contact-divider"></span>
        <span class="contact-item">
          <svg width="30" height="24" viewBox="0 0 24 19" aria-hidden="true"><path fill="#111" d="M2 0h20a2 2 0 0 1 2 2v15a2 2 0 0 1-2 2H2a2 2 0 0 1-2-2V2a2 2 0 0 1 2-2zm10 10 9-6V2l-9 6-9-6v2z"/></svg>
          mail@support
        </span>
      </div>
    </footer>
  </main>
</body>
</html>
```